Business Card Design

Electric home brewing equipment. Custom and catalog items. Most products are made by or for my company, so name is on most everything. Travel to conventions, to meet with home brewers. Trying to create a professional, but since primarily home brewers, fun image. New logo attached, with this new logo I'm redoing most materials. I'm trying to create a single brand under this logo.
Bolt icon on card, does not have to be directly over text as in logo file, but can be used similar to my example.

Website address is http://www.voltkettleworks.com (this is a must add).

New video intro to be added to video productions here: http://clipvault.example/k7Rm2xQwLp

Target Market(s)

Home brewers, predominantly male, ages 21 - 55, tend to be looking for the hot new thing.

Industry/Entity Type

Business

Contact Information for Business Card

Details as included on file. Layout I've attached is approximately what I'm looking for. Single and Double sided cards options welcome.

Card info should include:
2 cards: Derek Holm and Mona Holm
Both: Owners
Email: derek@voltkettleworks.com and mona@voltkettleworks.com
Both phone: 888-472-0635
Both address: Lakeview, Texas 77512
Website: voltkettleworks.com

Requirements
Must have
• Use both parts of the logo, not necessarily together as design should infer.

```html
<!DOCTYPE html>
<html lang="en">
<head>
<meta charset="utf-8">
<title>Volt Kettle Works – Business Cards</title>
<link rel="stylesheet" href="https://fonts.googleapis.com/css2?family=Arimo:wght@400;700&display=swap">
<style>
  :root {
    --stage: #1a0f10;
    --amber: #fbb905;
    --paper: #ffffff;
    --ink: #0d0d0d;
    --card-w: 300px;
    --card-h: 525px;
  }
  * { box-sizing: border-box; margin: 0; padding: 0; }
  html, body {
    width: 1200px; height: 1000px; overflow: hidden;
    background: var(--stage);
    font-family: "Arimo", Arial, sans-serif;
  }
  .stage {
    position: relative; width: 1200px; height: 1000px;
    display: flex; justify-content: center; align-items: center; gap: 80px;
  }
  .card {
    position: relative; width: var(--card-w); height: var(--card-h);
    background: var(--amber); overflow: hidden;
    box-shadow: 0 20px 50px rgba(0,0,0,.55);
  }
  .card__shapes { position: absolute; inset: 0; width: 100%; height: 100%; }
  .card__shapes .corner { fill: var(--ink); }
  .card__shapes .swoosh { fill: var(--paper); }
  .card__shapes .band { fill: var(--paper); }

  .brand-mark {
    position: absolute; border-radius: 50%; background: var(--amber);
  }
  .card--front .brand-mark {
    left: 50%; top: 95px; width: 150px; height: 150px; margin-left: -95px;
  }
  .card--back .brand-mark {
    left: 50%; top: 150px; width: 90px; height: 90px; margin-left: -45px;
  }

  .brand-name {
    position: absolute; left: 0; right: 0; text-align: center;
    font-weight: 700; font-size: 27px; letter-spacing: -0.5px;
    color: var(--ink); line-height: 1.1;
  }
  .card--front .brand-name { top: 362px; }
  .card--front .web {
    position: absolute; left: 0; right: 0; top: 455px; text-align: center;
    font-size: 15px; color: var(--paper);
  }

  .card--back .brand-name { top: 275px; }
  .contact {
    position: absolute; left: 0; right: 0; top: 398px; text-align: center;
    color: var(--paper); font-size: 14px; line-height: 1.35;
  }
  .contact__name { color: var(--ink); font-weight: 700; font-size: 16px; }
  .contact__role { color: var(--paper); }
  .contact__rule {
    width: 190px; height: 2px; background: var(--ink); margin: 6px auto 8px;
  }
</style>
</head>
<body>
<main class="stage">
  <section class="card card--front" aria-label="Card front">
    <svg class="card__shapes" viewBox="0 0 300 525" aria-hidden="true">
      <polygon class="corner" points="0,0 48,0 0,40"/>
      <ellipse class="swoosh" cx="110" cy="150" rx="200" ry="190"/>
      <rect class="band" x="0" y="335" width="300" height="88"/>
    </svg>
    <span class="brand-mark" aria-hidden="true"></span>
    <p class="brand-name">Volt Kettle Works</p>
    <p class="web">voltkettleworks.com</p>
  </section>

  <section class="card card--back" aria-label="Card back">
    <svg class="card__shapes" viewBox="0 0 300 525" aria-hidden="true">
      <polygon class="corner" points="0,0 60,0 0,60"/>
      <ellipse class="swoosh" cx="175" cy="110" rx="245" ry="270"/>
    </svg>
    <span class="brand-mark" aria-hidden="true"></span>
    <p class="brand-name">Volt Kettle Works</p>
    <div class="contact">
      <p class="contact__name">Mona Holm</p>
      <p class="contact__role">owner</p>
      <p class="contact__email">mona@voltkettleworks.com</p>
      <div class="contact__rule"></div>
      <p class="contact__phone">888-472-0635</p>
      <p class="contact__address">Lakeview, Texas 77512</p>
    </div>
  </section>
</main>
</body>
</html>
```